ReDesign for BrokerHarbor.net - Interactive, social, marketing site for Real Estate Pros!

Lets have fun with this... we are open to all ideas. Bring your "A" game and we will keep you busy in the future!

```html
<!DOCTYPE html>
<html lang="en">
<head>
<meta charset="utf-8">
<title>BrokerHarbor – Be a successful real estate agent</title>
<link href="https://fonts.googleapis.com/css2?family=Open+Sans:ital,wght@0,400;0,600;0,700;1,400;1,700&family=Handlee&display=swap" rel="stylesheet">
<style>
  :root{
    --navy:#1c3d4f;
    --navy-deep:#13313f;
    --teal:#3a7a99;
    --page:#f3f3f3;
    --ink:#2b2b2b;
    --field:#f7f7f7;
    --field-line:#d6d6d6;
    --bar:#d9d9d9;
    --orange:#f39a12;
    --rule:#bdbdbd;
  }
  *{box-sizing:border-box;margin:0;padding:0}
  html,body{width:1136px;height:1200px;overflow:hidden}
  body{background:var(--page);font-family:"Open Sans",Arial,sans-serif;color:var(--ink);position:relative}
  .abs{position:absolute}
  .top-bar{left:0;top:0;width:1136px;height:13px;background:var(--navy)}

  .brand{left:78px;top:40px;display:flex;align-items:center;gap:10px}
  .brand-mark{width:22px;height:22px;background:var(--navy)}
  .brand-name{font-size:50px;font-weight:600;color:var(--navy);letter-spacing:-1px;line-height:1}

  .login{left:644px;top:25px;display:flex;gap:6px;align-items:center}
  .login-field{height:23px;border:1px solid var(--field-line);background:#fff;border-radius:3px;font-size:11px;color:#999;padding:4px 8px}
  .login-btn{width:72px;height:23px;background:var(--navy);color:#fff;border-radius:3px;font-size:12px;font-weight:700;text-align:center;line-height:23px;margin-left:4px}
  .forgot{font-size:12px;font-weight:700;text-decoration:underline;color:var(--navy);margin-left:6px}

  .main-nav{left:505px;top:78px;width:563px;height:24px;border-bottom:3px solid #c9c9c9}
  .main-nav a{position:absolute;top:0;font-size:14px;color:var(--teal);text-decoration:none}
  .main-nav a.is-current{color:var(--navy)}

  .hero-title{left:78px;top:192px;font-size:32px;line-height:40px;color:var(--teal);font-weight:400;white-space:nowrap}
  .hero-title strong{color:var(--navy);font-weight:400}
  .hero-sub{left:82px;top:236px;font-size:15px;line-height:20px;color:var(--navy);white-space:nowrap}
  .feature{left:124px;display:flex;align-items:center;gap:26px}
  .feature-icon{width:48px;height:48px}
  .feature-label{font-family:"Handlee",cursive;font-size:22px;color:#444;border-bottom:3px solid #ccc;padding-bottom:2px}
  .hero-more{left:127px;top:463px;font-size:14px;color:#333;white-space:nowrap}

  .signup-head{left:669px;top:196px;width:383px;height:48px;background:#dcdcdc;font-size:31px;font-style:italic;color:var(--teal);padding:4px 12px;line-height:40px;white-space:nowrap}
  .signup-head b{color:var(--navy);font-weight:700}
  .form-label{left:676px;font-size:12px;font-style:italic;color:#333}
  .form-field{left:793px;width:252px;height:38px;background:var(--field);border:1px solid var(--field-line)}
  .next-btn{left:921px;top:469px;width:124px;height:41px;background:linear-gradient(#3a3a3a,#0c0c0c);color:#fff;border-radius:4px;font-size:15px;text-align:center;line-height:41px;letter-spacing:-.5px}

  .section-head{width:298px;font-size:19px;font-weight:700;color:var(--navy);padding-bottom:4px;border-bottom:6px solid var(--navy);display:flex;gap:14px;align-items:center}
  .section-head .arrow{font-size:16px}
  .section-text{font-family:Arial,Helvetica,sans-serif;font-size:13px;line-height:19px;color:#444;text-align:justify}
  .read-more{left:83px;top:738px;font-family:Arial,Helvetica,sans-serif;font-size:13px;font-weight:700;color:var(--orange)}
  .tick{left:415px;top:618px;width:17px;height:17px;background:#c8c8c8}
  .closing{left:444px;top:730px;font-family:Arial,Helvetica,sans-serif;font-size:13px;font-weight:700;color:#444}

  .member{left:750px;display:flex;align-items:center;gap:8px}
  .member-avatar{width:22px;height:28px;background:linear-gradient(#d0d0d0,#bcbcbc);border-radius:11px 11px 3px 3px}
  .member-name{width:261px;height:26px;background:var(--bar);font-family:Arial,Helvetica,sans-serif;font-size:13.5px;color:#333;line-height:26px;padding-left:14px;text-transform:uppercase}

  .divider{left:86px;top:795px;width:954px;height:2px;background:var(--rule)}
  .tour{top:853px;width:215px;height:135px;border:1px solid #bbb;background:#fff;padding:4px}
  .tour-photo{width:100%;height:100%}
  .tour-view{position:absolute;right:7px;bottom:7px;width:62px;height:22px;background:var(--orange);color:#222;font-size:12px;font-weight:700;text-align:center;line-height:22px}

  .social{font-weight:700;color:var(--navy);line-height:1.2}
  .social-chirper{left:150px;top:1046px;font-size:30px}
  .social-sociala{left:412px;top:1046px;font-size:22px;line-height:26px}
  .social-sociala small{display:block;font-size:14px;line-height:18px;font-weight:600}

  .footer{left:0;top:1098px;width:1136px;height:102px;background:var(--navy-deep)}
  .footer-line{position:absolute;top:14px;font-size:12px;color:#fff;white-space:nowrap}
  .footer-sep{position:absolute;left:784px;top:12px;width:1px;height:22px;background:#8aa0ac}
</style>
</head>
<body>
  <div class="abs top-bar"></div>

  <div class="abs brand"><span class="brand-mark"></span><span class="brand-name">BrokerHarbor</span></div>

  <div class="abs login">
    <div class="login-field" style="width:107px">Username</div>
    <div class="login-field" style="width:110px">Password</div>
    <div class="login-btn">Login</div>
    <span class="forgot">Forgot Password?</span>
  </div>

  <nav class="abs main-nav">
    <a class="is-current" style="left:40px">HOME</a>
    <a style="left:125px">ABOUT</a>
    <a style="left:214px">MEMBERSHIP</a>
    <a style="left:338px">TOOLS</a>
    <a style="left:425px">BLOG</a>
    <a style="left:505px">CONTACT</a>
  </nav>

  <h1 class="abs hero-title">Be a <strong>SUCCESSFUL</strong> real estate agent</h1>
  <p class="abs hero-sub">we help you build a career through collaboration and use of valuable tools.</p>

  <div class="abs feature" style="top:268px">
    <svg class="feature-icon" viewBox="0 0 48 48"><circle cx="24" cy="24" r="22" fill="#9a9a9a" stroke="#777" stroke-width="2"/><path d="M19 14 L34 24 L19 34Z" fill="#555"/></svg>
    <span class="feature-label">Unlimited Virtual Tour</span>
  </div>
  <div class="abs feature" style="top:331px">
    <div class="feature-icon" role="img" aria-label="Group of people networking icon" style="background:radial-gradient(circle,#8a8a8a,#c8c8c8);border-radius:50%"></div>
    <span class="feature-label">Professional Networking</span>
  </div>
  <div class="abs feature" style="top:395px">
    <svg class="feature-icon" viewBox="0 0 48 48"><rect x="4" y="4" width="40" height="40" fill="#8d8d8d"/></svg>
    <span class="feature-label">Sociala Integration</span>
  </div>
  <p class="abs hero-more">mapsy street views, &nbsp;professional listing flyers, video creations, and more..</p>

  <div class="abs signup-head">Sign up now for <b>FREE!</b></div>
  <span class="abs form-label" style="top:270px">First Name</span>
  <div class="abs form-field" style="top:257px"></div>
  <span class="abs form-label" style="top:312px">Last Name</span>
  <div class="abs form-field" style="top:299px"></div>
  <span class="abs form-label" style="top:354px">Email Address</span>
  <div class="abs form-field" style="top:342px"></div>
  <span class="abs form-label" style="top:396px">Your Password</span>
  <div class="abs form-field" style="top:384px"></div>
  <span class="abs form-label" style="top:438px">Re-enter Password</span>
  <div class="abs form-field" style="top:425px"></div>
  <div class="abs next-btn">NEXT STEP</div>

  <h2 class="abs section-head" style="left:83px;top:558px"><span class="arrow">→</span>ABOUT US</h2>
  <p class="abs section-text" style="left:83px;top:614px;width:298px">We have developed the most Agent friendly, dynamic set of tools to empower the real estate industry. Inside, you will find real estate professionals networking, exchanging ideas and learning from each other to better themselves and build a more profitable environment for everyone.</p>
  <span class="abs read-more">READ MORE..</span>

  <h2 class="abs section-head" style="left:415px;top:558px"><span class="arrow">→</span>FEATURED TOOLS</h2>
  <svg class="abs tick" viewBox="0 0 17 17"><path d="M4 9 L7 12 L13 5" fill="none" stroke="#444" stroke-width="1.6"/></svg>
  <p class="abs section-text" style="left:444px;top:614px;width:270px">BrokerHarbor provides you with simple solutions to promote your listings anywhere! You can add your Virtual Tour to any website! Anywhere you want to promote your virtual tour is up to you, It is easy to manage and easy to use.</p>
  <span class="abs closing">WE HOPE YOU ENJOY IT!</span>

  <h2 class="abs section-head" style="left:745px;top:558px"><span class="arrow">→</span>NEW MEMBERS</h2>
  <div class="abs member" style="top:622px"><span class="member-avatar" role="img" aria-label="Member avatar"></span><span class="member-name">Dorin Mateescu</span></div>
  <div class="abs member" style="top:654px"><span class="member-avatar" role="img" aria-label="Member avatar"></span><span class="member-name">Helen Brooks</span></div>
  <div class="abs member" style="top:687px"><span class="member-avatar" role="img" aria-label="Member avatar"></span><span class="member-name">Marina Lowell</span></div>
  <div class="abs member" style="top:720px"><span class="member-avatar" role="img" aria-label="Member avatar"></span><span class="member-name">Peter Hanlon</span></div>

  <div class="abs divider"></div>
  <h2 class="abs section-head" style="left:86px;top:814px;border:0;width:auto"><span class="arrow">→</span>LATEST VIRTUAL TOOLS</h2>

  <div class="abs tour" style="left:87px"><div class="tour-photo" role="img" aria-label="Modern glass office building under blue sky" style="background:linear-gradient(#1f56b8 0%,#5a8fd6 45%,#d8dde4 75%,#8a8f96 100%)"></div><span class="tour-view">VIEW →</span></div>
  <div class="abs tour" style="left:331px"><div class="tour-photo" role="img" aria-label="Brick family house with gray roof and garden" style="background:linear-gradient(#2d66c4 0%,#7aa3df 35%,#8a7a6a 60%,#4f6b3a 100%)"></div><span class="tour-view">VIEW →</span></div>
  <div class="abs tour" style="left:574px"><div class="tour-photo" role="img" aria-label="Cream colonial house among green trees" style="background:linear-gradient(#9fc4ea 0%,#3f7a2f 35%,#d8d2b8 60%,#4e7c34 100%)"></div><span class="tour-view">VIEW →</span></div>
  <div class="abs tour" style="left:820px"><div class="tour-photo" role="img" aria-label="Contemporary white villa with palm trees" style="background:linear-gradient(#eceff2 0%,#cfcac2 40%,#6d5a48 65%,#9aa09a 100%)"></div><span class="tour-view">VIEW →</span></div>

  <div class="abs social social-chirper">Chirper</div>
  <div class="abs social social-sociala"><small>Find us on</small>Sociala</div>

  <footer class="abs footer">
    <span class="footer-line" style="left:632px">BROKERHARBOR © 2011</span>
    <span class="footer-sep"></span>
    <span class="footer-line" style="left:798px">Home</span>
    <span class="footer-line" style="left:842px">Blog</span>
    <span class="footer-line" style="left:878px">Privacy</span>
    <span class="footer-line" style="left:929px">Terms</span>
    <span class="footer-line" style="left:974px">Feedback</span>
  </footer>
</body>
</html>
```